Mission statement design for a secondary school

We have the content of our mission statement and need an appealing layout. The design should fit on a poster or A4 page. The content grouping in the document should also be graphically recognizable. Our target group are young people and their parents as well as the school staff, which is why we need a modern design that is not out after 2 years. It must be easy to grasp visually and graphically simple.

Target Market(s)

Actors of the school

Requirements
Must have
• cantonal logo including school name see document can be integrated as a header
Should not have
• References to trademarks or third parties

```html
<!DOCTYPE html>
<html lang="de">
<head>
<meta charset="utf-8">
<title>Our Mission Statement</title>
<link rel="stylesheet" href="https://fonts.googleapis.com/css2?family=Anton&family=Montserrat:wght@600;700&display=swap">
<style>
  :root {
    --red: #e42614;
    --ink: #222222;
    --panel-grey: #e9e9e9;
    --tab-grey: #bdbdbd;
    --page: #ffffff;
    --pattern-light: #f7f7f7;
    --pattern-mid: #e2e2e2;
  }
  * { box-sizing: border-box; margin: 0; padding: 0; }
  html, body { width: 864px; height: 1200px; overflow: hidden; background: var(--page); }
  .poster {
    position: relative; width: 864px; height: 1200px; overflow: hidden;
    font-family: "Montserrat", sans-serif; color: var(--ink);
    background: var(--page);
  }
  .side-pattern {
    position: absolute; left: 0; top: 0; width: 289px; height: 1200px;
    background: linear-gradient(170deg, var(--pattern-light) 0%, var(--pattern-mid) 45%, var(--pattern-light) 75%, var(--page) 100%);
  }
  .brand {
    position: absolute; left: 30px; top: 66px; width: 222px; text-align: right;
    font-family: "Montserrat", sans-serif; font-weight: 700; color: var(--red);
  }
  .brand-name { font-size: 16px; line-height: 20px; letter-spacing: 0.5px; }
  .brand-dept { margin-top: 10px; font-size: 8px; line-height: 11px; letter-spacing: 0.3px; }
  .title-band {
    position: absolute; left: 289px; top: 50px; width: 575px; height: 85px;
    background: var(--red); color: #fff;
    font-family: "Anton", sans-serif; font-size: 47px; letter-spacing: -0.5px;
    display: flex; align-items: center; justify-content: center;
  }
  .tab {
    position: absolute; left: 44px; width: 210px; height: 58px;
    background: var(--tab-grey);
    display: flex; align-items: center; justify-content: center; gap: 8px;
    font-weight: 600; font-size: 15px; letter-spacing: 0.8px; color: var(--ink);
  }
  .tab::after {
    content: ""; position: absolute; right: -16px; top: 18px;
    border-left: 16px solid var(--tab-grey);
    border-top: 11px solid transparent; border-bottom: 11px solid transparent;
  }
  .tab-icon { width: 18px; height: 18px; border-radius: 50%; background: var(--ink); }
  .section {
    position: absolute; left: 289px; width: 575px; padding-left: 143px; padding-right: 20px;
  }
  .section-grey { background: var(--panel-grey); color: var(--ink); }
  .section-red { background: var(--red); color: #fff; }
  .section h2 {
    font-weight: 700; font-size: 25px; letter-spacing: 1px; line-height: 1;
    margin-left: -95px;
  }
  .section .lead { margin-left: -95px; margin-top: 6px; font-weight: 600; font-size: 13.5px; }
  .points { list-style: none; margin-left: -95px; }
  .points li {
    position: relative; padding-left: 31px;
    font-weight: 600; font-size: 13.4px; line-height: 15.5px; margin-bottom: 10.2px;
  }
  .section-red .points li { font-weight: 700; }
  .points svg { position: absolute; left: 0; top: 2px; width: 9px; height: 9px; }
</style>
</head>
<body>
<div class="poster">
  <div class="side-pattern" role="img" aria-label="Dezentes graues Punkt- und Rautenmuster als Hintergrund"></div>

  <div class="brand">
    <div class="brand-name">Nordtal Land</div>
    <div class="brand-dept">DEPARTEMENT SCHULE UND FREIZEIT<br>FACHSTELLE SCHULSPORT</div>
  </div>

  <div class="title-band">OUR MISSION STATEMENT</div>

  <div class="tab" style="top:229px">HALTUNG <span class="tab-icon" role="img" aria-label="Symbol Haltung"></span></div>
  <div class="tab" style="top:484px">LERNEN <span class="tab-icon" role="img" aria-label="Symbol Lernen"></span></div>
  <div class="tab" style="top:746px">ENTWICKLUNG <span class="tab-icon" role="img" aria-label="Symbol Entwicklung"></span></div>
  <div class="tab" style="top:1010px">GEMEINSCHAFT <span class="tab-icon" role="img" aria-label="Symbol Gemeinschaft"></span></div>

  <svg width="0" height="0" style="position:absolute">
    <defs>
      <symbol id="tick-dark" viewBox="0 0 10 10"><circle cx="5" cy="5" r="5" fill="#222"/><path d="M2.6 5.2 4.3 6.8 7.4 3.6" stroke="#fff" stroke-width="1.5" fill="none"/></symbol>
      <symbol id="tick-light" viewBox="0 0 10 10"><circle cx="5" cy="5" r="5" fill="#fff"/><path d="M2.6 5.2 4.3 6.8 7.4 3.6" stroke="#e42614" stroke-width="1.5" fill="none"/></symbol>
    </defs>
  </svg>

  <section class="section section-grey" style="top:135px;height:220px;padding-top:31px">
    <h2>HALTUNG</h2>
    <p class="lead">An unserer Schule</p>
    <ul class="points" style="margin-top:18px">
      <li><svg><use href="#tick-dark"/></svg>Stehen die Lernenden im Mittelpunkt.</li>
      <li><svg><use href="#tick-dark"/></svg>Ist Integration selbstverständlich.</li>
      <li><svg><use href="#tick-dark"/></svg>Begegnen wir uns respektvoll und wertschätzend.</li>
      <li><svg><use href="#tick-dark"/></svg>Setzen wir uns für lebenslanges Lernen ein.</li>
    </ul>
  </section>

  <section class="section section-red" style="top:355px;height:296px;padding-top:22px">
    <h2>LERNEN</h2>
    <ul class="points" style="margin-top:15px">
      <li><svg><use href="#tick-light"/></svg>Wir begleiten unsere Lernenden hin zur Selbständigkeit.</li>
      <li><svg><use href="#tick-light"/></svg>Wir unterstützen unsere Lernenden in ihrem individuellen Kompetenzerwerb.</li>
      <li><svg><use href="#tick-light"/></svg>Wir ermöglichen allen Lernenden Erfolge.</li>
      <li><svg><use href="#tick-light"/></svg>Die Unterrichtsinhalte orientieren sich an aktuellen Themen.</li>
      <li><svg><use href="#tick-light"/></svg>Wir beurteilen transparent.</li>
      <li><svg><use href="#tick-light"/></svg>Wir begegnen Heterogenität mit multiprofessionellen Teams.</li>
      <li><svg><use href="#tick-light"/></svg>Wir schaffen eine wertschätzende und förderliche Atmosphäre.</li>
      <li><svg><use href="#tick-light"/></svg>Unsere Schule bietet eine zeitgemässe Infrastruktur.</li>
    </ul>
  </section>

  <section class="section section-grey" style="top:651px;height:249px;padding-top:15px">
    <h2>ENTWICKLUNG</h2>
    <ul class="points" style="margin-top:16px">
      <li><svg><use href="#tick-dark"/></svg>Wir entwickeln unsere Schule gemeinsam.</li>
      <li><svg><use href="#tick-dark"/></svg>Wir setzen unsere Fähigkeiten und Kräfte gezielt ein.</li>
      <li><svg><use href="#tick-dark"/></svg>Alle tragen Verantwortung.</li>
      <li><svg><use href="#tick-dark"/></svg>Wir lernen alle voneinander.</li>
      <li><svg><use href="#tick-dark"/></svg>Wir bilden uns kontinuierlich weiter.</li>
      <li><svg><use href="#tick-dark"/></svg>Wir reflektieren unser Handeln.</li>
      <li><svg><use href="#tick-dark"/></svg>Wir sind innovativ und gehen mutig unseren Weg.</li>
    </ul>
  </section>

  <section class="section section-red" style="top:900px;height:259px;padding-top:25px">
    <h2>GEMEINSCHAFT</h2>
    <ul class="points" style="margin-top:18px">
      <li><svg><use href="#tick-light"/></svg>Unsere Schule achtet die Gesundheit aller.</li>
      <li><svg><use href="#tick-light"/></svg>Wir legen Wert auf eine offene Kommunikation.</li>
      <li><svg><use href="#tick-light"/></svg>Unsere pädagogische Zusammenarbeit basiert auf einer professionellen Haltung.</li>
      <li><svg><use href="#tick-light"/></svg>Die Eltern sind ein Teil unserer Schulgemeinschaft und tragen Verantwortung.</li>
      <li><svg><use href="#tick-light"/></svg>Wir haben an unserer Schule Freiräume innerhalb klarer Rahmenbedingungen.</li>
    </ul>
  </section>
</div>
</body>
</html>
```